Design einer Frühjahrsbroschüre für Immobilienmakler
Zielgruppe
Wir sind Immobilienmakler und möchten eine neue Frühjahrsbroschüre verteilen lassen.
Wir haben über Entwurfsmarkt schon mehrere Projekte gemacht und waren immer zufrieden.
Unsere Zielgruppe sind Immobilienverkäufer.
Aufgabenstellung
Der Flyer soll die Größe haben DinA3 auf DinA4 gefaltet. Somit sind 4 DinA4 Seiten zu gestallten.
Bei Papier im Fluss soll gedruckt werden. https://www.papier-im-fluss.de/faltblatt-gefalzt-auf-din-a4-4seiter.html#content-view
1. Seite: Frühlingshaft und ansprechende Aufmachung. Harmonische Farben. Ein Slogan.
Frühjahrsaktion: Verkäufer erhält nach Verkauf als Dankeschön für den Auftrag und sein Vertrauen in uns einen neuen Kochwerk KX4 oder 1000€ in bar.
2. Immobilienverkauf in Coronazeiten.
Warum Verkaufen mit Nord-Immobilien Kaltenbach
3. Aktuelle Immobilienangebote
4. Wir suchen für unsere Kunden
Im Anhang sind andere Flyer/Broschüren die uns seither gut gefallen haben.

```html
<!DOCTYPE html>
<html lang="de">
<head>
<meta charset="utf-8">
<title>Frühjahrsaktion – Nord-Immobilien Kaltenbach</title>
<link href="https://fonts.googleapis.com/css2?family=Roboto:wght@400;700;900&display=swap" rel="stylesheet">
<style>
  :root{
    --navy:#1b5870;
    --green:#12a98a;
    --white:#ffffff;
    --ink:#1b5870;
  }
  *{margin:0;padding:0;box-sizing:border-box}
  html,body{width:1200px;height:600px;overflow:hidden;background:var(--white)}
  .flyer{position:relative;width:1200px;height:600px;overflow:hidden;font-family:"Roboto",Arial,sans-serif;color:var(--ink)}
  .backdrop{position:absolute;inset:0}
  .txt{position:absolute;text-align:center;line-height:1.35}
  .intro{right:58px;top:8px;text-align:right;color:var(--white);font-size:19px;line-height:24px}
  .intro span{display:block}
  .section-title{left:680px;width:464px;top:60px;color:var(--white);font-weight:700;font-size:26px;letter-spacing:.2px}
  .reasons{left:50px;width:500px;top:103px}
  .reasons h3{font-weight:900;font-size:17.5px;letter-spacing:.3px;text-transform:uppercase;line-height:22px}
  .reasons p{font-size:16.5px;line-height:22px;margin-bottom:15px}
  .headline{right:38px;top:438px;color:var(--white);font-weight:900;font-size:57px;letter-spacing:0;line-height:57px;white-space:nowrap;text-align:right;transform:scaleX(.9);transform-origin:right center}
  .no-fee{left:95px;width:500px;top:504px}
  .no-fee h3{color:var(--green);font-weight:900;font-size:25px;line-height:28px}
  .no-fee p{font-size:16.5px;line-height:23px}
  .reward{left:620px;width:570px;top:505px;font-size:20px;line-height:25px}
  .reward .amount{color:var(--green);font-size:36px;line-height:25px;vertical-align:-4px}
  .brand{position:absolute;left:1012px;top:356px;display:flex;align-items:center;gap:8px}
  .brand-mark{width:14px;height:14px;border-radius:50%;background:var(--navy)}
  .brand-name{font-weight:700;font-size:17px;line-height:20px;color:var(--navy)}
</style>
</head>
<body>
<main class="flyer">
  <svg class="backdrop" viewBox="0 0 1200 600" width="1200" height="600">
    <defs>
      <linearGradient id="sky" x1="0" y1="0" x2="1" y2="1">
        <stop offset="0" stop-color="#a9c49a"/><stop offset=".6" stop-color="#dfe7bf"/><stop offset="1" stop-color="#8fae7b"/>
      </linearGradient>
      <linearGradient id="meadow" x1="0" y1="0" x2="1" y2="1">
        <stop offset="0" stop-color="#6f7d45"/><stop offset=".5" stop-color="#a29a5e"/><stop offset="1" stop-color="#5a7656"/>
      </linearGradient>
      <linearGradient id="villa" x1="0" y1="0" x2="1" y2="1">
        <stop offset="0" stop-color="#2e5566"/><stop offset=".45" stop-color="#b7a054"/><stop offset=".8" stop-color="#4f7a4f"/><stop offset="1" stop-color="#2f5a3d"/>
      </linearGradient>
    </defs>
    <g role="img" aria-label="Frühlingswiese mit Gräsern im Gegenlicht">
      <rect x="0" y="330" width="1200" height="270" fill="url(#meadow)"/>
      <rect x="330" y="0" width="560" height="110" fill="url(#sky)"/>
    </g>

    <polygon points="0,0 375,0 340,57 0,57" fill="var(--navy)"/>
    <polygon points="825,0 1200,0 1200,57 860,57" fill="var(--navy)"/>
    <polygon points="0,57 27,57 262,430 0,430" fill="var(--white)"/>
    <polygon points="27,57 60,57 290,420 285,430 262,430" fill="var(--navy)"/>

    <g role="img" aria-label="Moderne Villa mit Glasfassade und Balkon, im Grünen gelegen">
      <rect x="600" y="99" width="540" height="242" fill="url(#villa)"/>
    </g>
    <g role="img" aria-label="Hellere, verblasste Ansicht desselben Hauses hinter dem Text">
      <rect x="50" y="99" width="550" height="242" fill="#eef1ef"/>
    </g>

    <polygon points="58,57 521,57 497,99 80,99" fill="var(--green)"/>
    <polygon points="235,341 345,341 290,430" fill="var(--green)"/>
    <polygon points="462,341 482,341 430,430 404,430" fill="var(--navy)"/>
    <polygon points="482,341 720,341 768,430 432,430" fill="var(--green)"/>
    <polygon points="720,341 745,341 800,430 768,430" fill="var(--navy)"/>
    <polygon points="1143,57 1182,57 935,430 900,430" fill="var(--navy)"/>
    <polygon points="1182,57 1200,57 1200,430 935,430" fill="var(--white)"/>
    <polygon points="680,57 1143,57 1120,99 705,99" fill="var(--green)"/>
    <polygon points="855,341 980,341 910,430" fill="var(--green)"/>
    <polygon points="404,430 1200,430 1200,494 380,494" fill="var(--navy)"/>
    <polygon points="0,430 108,430 0,590" fill="var(--navy)"/>
    <polygon points="105,494 1200,494 1200,600 45,600" fill="var(--white)"/>
  </svg>

  <div class="txt intro"><span>Aktuelle Immobilienangebote</span><span>Wir suchen für unsere Kunden</span></div>
  <h2 class="txt section-title">Immobilienverkauf in Coronazeiten</h2>

  <section class="txt reasons">
    <h3>Warum mit Nord-Immobilien verkaufen?</h3>
    <p>Unser Versprechen: 100 % Maklerservice, 0 % Provisionsschmerz</p>
    <h3>Erfahrene Makler</h3>
    <p>Wir kommen aus der Region und kennen den lokalen<br>Immobilienmarkt seit Jahren.</p>
    <h3>Volle Serviceleistung</h3>
    <p>Ihr lokaler Makler steht<br>Ihnen bei jedem Schritt des Verkaufs zur Seite:<br>von der Bewertung und Bewerbung bis zur Schlüsselübergabe.</p>
  </section>

  <div class="brand">
    <span class="brand-mark"></span>
    <span class="brand-name">Nord-Immobilien<br>Kaltenbach</span>
  </div>

  <h1 class="txt headline">FRÜHJAHRSAKTION</h1>

  <section class="txt no-fee">
    <h3>KEINE VERKAUFSPROVISION</h3>
    <p>Der gesamte Service ist bei uns für Verkäufer kostenfrei.<br>Auch Käufer zahlen weniger Provision als marktüblich.</p>
  </section>

  <p class="txt reward">Verkäufer erhält nach Verkauf als Dankeschön<br>für den Auftrag und sein Vertrauen<br>in uns einen neuen Kochwerk KX4 oder <span class="amount">1000€</span> in bar.</p>
</main>
</body>
</html>
```